Packaging design pot 500gr Polynesian honey

Task Description

Concept of design:

"This Polynesian island is a small piece of paradise nestled in the South Pacific, away from any form of civilization ( ideal place for producing honey of excellence )
= Images / symbols that induces dreaming)); (100% organic, 100% natural organic Honey logo)
Elegant, subtle , eyes catching, NO pictures of bees , Simple colors: BLACK, GOLD, WHITE, tranparency . (Designer discretion)
(Bio label optional )

the Labels: Hex1 product of ORAVAI header: VELINOA HONEY (brand name) MAY USE all images herein below , free of copyright (Macro coconut flower, coconut white sand beach, exoticism; 500 gr; text on back (see attached text); Position the bar code vertically on the back; Mandatory address: Website on the back, infocontact, registration number.

500g pot :
HEIGHT With cap 12.00cm Without cap 11.85 cm
outside diameter 7.24cm
Label height should only be = 5, 1 cm x height
See the container with black cap.

Deadline
March 15, 2018 ( postpone if needed )
Updates

To all participants, i have added a personal photo you may want to consider in your creative process. If the upper section of the photo is exploited, I thought it has something interesting to bring: blue sky on the background including a shadow ot the coconut leaves, ( no bees please).

Finally i have added the colour of Velinoa Honey

Dear participants, I have updated two files to be taken into account onward : 1) final text: in French ; the replicate is English for the English version valid with the identical Graphic design 2) the true colours of Velinoa Honey, for your consideration. I thought that with the help of day light i could enhance its true body colour. Best regards, Mr KOR

Target Market(s)

Target the Asian market , Onward The US MARKET, (LUXURY oriented)

Font styles to use
Serif

Colors

Designer to choose colors to be used in the design.

Requirements
Must have
• Website address on the back, infocontact, registration number,
• texte ( summary )
• coconut tree honey ( ORIGIN )
• Color code : BLACK , GOLD , light , transparency
• COLORS THAT MATCH COLOR OF THE HONEY : DARK RED AMBER SEE IMAGE ATTACHED
Nice to have
• A matching logo
• A 400g Squezze bottle format ;
• h18.5*d7.8*c3.2(cm)
Should not have
• No Bees

```html
<!DOCTYPE html>
<html lang="en">
<head>
<meta charset="utf-8">
<title>Oravai 100% Honey – Jar Label</title>
<link rel="stylesheet" href="https://fonts.googleapis.com/css2?family=Alfa+Slab+One&family=Old+Standard+TT:wght@400;700&family=Roboto:wght@700&display=swap">
<style>
  :root {
    --backdrop: #f1efec;
    --label-white: #ffffff;
    --ink: #1c1a1a;
    --seal-dark: #2a2626;
    --sand: #e9e1d2;
    --sea: #a9cfd6;
    --coconut-gold: #e2a855;
    --husk-brown: #7a5233;
  }
  html, body {
    margin: 0;
    padding: 0;
    width: 1200px;
    height: 1200px;
    overflow: hidden;
    background: var(--backdrop);
  }
  .label-canvas {
    display: block;
    width: 1200px;
    height: 1200px;
  }
  .arched-brand {
    font-family: "Old Standard TT", Georgia, serif;
    font-size: 80px;
    letter-spacing: 22px;
    fill: var(--ink);
  }
  .arched-origin {
    font-family: "Old Standard TT", Georgia, serif;
    font-size: 70px;
    letter-spacing: 30px;
    fill: var(--ink);
  }
  .stars {
    font-family: "Old Standard TT", Georgia, serif;
    font-size: 40px;
    letter-spacing: 6px;
    fill: var(--ink);
  }
  .product-name {
    font-family: "Alfa Slab One", Georgia, serif;
    font-size: 112px;
    fill: var(--ink);
  }
  .qualities {
    font-family: "Old Standard TT", Georgia, serif;
    font-size: 42px;
    letter-spacing: 7px;
    fill: var(--ink);
  }
  .net-weight {
    font-family: "Roboto", Arial, sans-serif;
    font-weight: 700;
    font-size: 46px;
    fill: var(--ink);
  }
  .rule { stroke: var(--ink); }
</style>
</head>
<body>
<svg class="label-canvas" viewBox="0 0 1200 1200" xmlns="http://www.w3.org/2000/svg">
  <defs>
    <linearGradient id="island-scene" x1="0" y1="0" x2="1" y2="0">
      <stop offset="0" stop-color="var(--sea)"/>
      <stop offset="0.3" stop-color="var(--sand)"/>
      <stop offset="0.62" stop-color="var(--sand)"/>
      <stop offset="0.8" stop-color="var(--coconut-gold)"/>
      <stop offset="1" stop-color="var(--husk-brown)"/>
    </linearGradient>
    <clipPath id="scene-band-clip">
      <rect x="94" y="680" width="1001" height="330"/>
    </clipPath>
    <path id="brand-arc" d="M 300 592 A 300 300 0 0 1 900 592"/>
    <path id="origin-arc" d="M 215 592 A 385 385 0 0 0 985 592"/>
  </defs>

  <!-- label body -->
  <g class="label-body">
    <path d="M 160 592 A 440 440 0 0 1 1040 592 Z" fill="var(--label-white)"/>
    <rect x="94" y="530" width="1001" height="150" fill="var(--label-white)"/>
    <rect x="94" y="1010" width="1001" height="58" fill="var(--label-white)"/>
  </g>

  <!-- island scene band -->
  <rect x="94" y="680" width="1001" height="330" fill="url(#island-scene)" role="img" aria-label="Photo of a white sand beach with palm leaves and an opened coconut"/>
  <circle cx="600" cy="592" r="440" fill="var(--label-white)" opacity="0.45" clip-path="url(#scene-band-clip)"/>

  <!-- upper band rules -->
  <line class="rule" x1="94" y1="541" x2="1095" y2="541" stroke-width="8"/>
  <line class="rule" x1="94" y1="562" x2="1095" y2="562" stroke-width="3"/>

  <!-- arched brand name -->
  <text class="arched-brand"><textPath href="#brand-arc" startOffset="50%" text-anchor="middle">ORAVAI</textPath></text>

  <!-- seal -->
  <circle cx="600" cy="383" r="77" fill="var(--seal-dark)"/>
  <circle cx="600" cy="383" r="64" fill="none" stroke="var(--label-white)" stroke-width="3"/>

  <text class="stars" x="369" y="480" text-anchor="middle">★★★</text>
  <text class="stars" x="831" y="480" text-anchor="middle">★★★</text>

  <!-- product name -->
  <text class="product-name" x="600" y="660" text-anchor="middle" textLength="770" lengthAdjust="spacingAndGlyphs">100% HONEY</text>

  <!-- qualities box -->
  <g class="qualities-box">
    <line class="rule" x1="248" y1="718" x2="941" y2="718" stroke-width="3"/>
    <rect x="248" y="728" width="693" height="62" fill="none" stroke="var(--ink)" stroke-width="3"/>
    <line class="rule" x1="532" y1="728" x2="532" y2="790" stroke-width="3"/>
    <line class="rule" x1="700" y1="728" x2="700" y2="790" stroke-width="3"/>
    <text class="qualities" x="390" y="775" text-anchor="middle">NATURAL</text>
    <text class="qualities" x="616" y="775" text-anchor="middle">RAW</text>
    <text class="qualities" x="820" y="775" text-anchor="middle">PURE</text>
  </g>

  <text class="net-weight" x="600" y="866" text-anchor="middle">500 GR</text>

  <text class="arched-origin"><textPath href="#origin-arc" startOffset="50%" text-anchor="middle">COCONUT</textPath></text>

  <!-- lower band rules -->
  <line class="rule" x1="94" y1="1028" x2="1095" y2="1028" stroke-width="3"/>
  <line class="rule" x1="94" y1="1046" x2="1095" y2="1046" stroke-width="8"/>
</svg>
</body>
</html>
```